Web Application UI Design

Looking for a light weight UI re-design with complete html files and images for an existing project. As you can see from the uploaded files, the current design is clunky. We are looking to redesign the web application with state of the art light weight UI (Must include bootstrap and should be able to support angular)

Requirements
Must have
• Must have lightweight design preferably with material and bootstrap design
Nice to have
• The screen shots I uploaded show that the design is clunky. I am looking for some new designs

```html
<!DOCTYPE html>
<html lang="en">
<head>
<meta charset="utf-8">
<title>Nexa form – Projects</title>
<link href="https://fonts.googleapis.com/css2?family=Inter:wght@300;400;500;600;700&display=swap" rel="stylesheet">
<style>
:root{
  --brand:#5059fe;
  --brand-strong:#4b55f7;
  --page:#eef0fb;
  --panel:#ffffff;
  --content:#fbfbfe;
  --active:#f3f4fd;
  --text:#555a66;
  --text-soft:#7c7f88;
  --text-faint:#b9bcc4;
  --line:#ececf2;
  --badge-blue:#8fb0ff;
  --badge-pink:#e48bf7;
  --badge-green:#7ef07a;
  --badge-red:#ff7b9b;
}
*{box-sizing:border-box;margin:0;padding:0}
html,body{width:1200px;height:943px;overflow:hidden}
body{background:var(--page);font-family:"Inter",Arial,sans-serif;position:relative}
.app{position:absolute;left:144px;top:15px;width:1013px;height:1013px;transform:scale(.9);transform-origin:0 0;background:var(--content);box-shadow:0 20px 60px rgba(60,70,180,.15);overflow:hidden}
.topbar{position:absolute;left:0;top:0;width:100%;height:70px;background:var(--brand)}
.topbar h1{position:absolute;left:285px;top:22px;font-size:21px;font-weight:300;color:#fff;letter-spacing:.2px}
.topbar h1 b{font-weight:700}
.sidebar{position:absolute;left:0;top:70px;width:259px;bottom:0;background:var(--panel);box-shadow:2px 0 8px rgba(0,0,0,.03)}
.profile{position:absolute;left:0;top:0;width:100%;height:117px;border-bottom:1px solid var(--line)}
.avatar{position:absolute;left:23px;top:18px;width:54px;height:54px;border-radius:50%;background:radial-gradient(circle at 50% 40%,#6b5a4a,#2f3a2c)}
.profile .name{position:absolute;left:89px;top:36px;font-size:16px;color:var(--text);font-weight:500}
.profile .role{position:absolute;left:89px;top:61px;font-size:12px;color:var(--text-faint);font-weight:500}
.profile .caret{position:absolute;left:210px;top:46px}
.nav{list-style:none}
.nav-item{position:absolute;left:0;width:100%;height:20px;display:flex;align-items:center}
.nav-item svg{position:absolute;left:15px;width:18px;height:18px}
.nav-item .label{position:absolute;left:50px;font-size:14px;color:var(--text);font-weight:500}
.badge{position:absolute;left:223px;width:17px;height:17px;font-size:12px;font-weight:600;color:#fff;text-align:center;line-height:17px}
.group{position:absolute;left:0;top:328px;width:100%;height:214px;background:var(--active)}
.nav-item.active .label{color:var(--brand)}
.sub{position:absolute;left:77px;font-size:14px;color:var(--text);font-weight:500}
.create-btn{position:absolute;left:808px;top:126px;width:182px;height:36px;border-radius:18px;background:var(--brand-strong);color:#fff;font-size:14px;font-weight:600;text-align:center;line-height:36px;box-shadow:0 8px 16px rgba(75,85,247,.3)}
.card{position:absolute;width:219px;height:154px;background:#fff;border-radius:3px;box-shadow:0 2px 8px rgba(40,50,120,.09)}
.card h3{position:absolute;left:15px;top:12px;font-size:11px;font-weight:500;color:#333;letter-spacing:.1px}
.card .kebab{position:absolute;right:14px;top:9px}
.card hr{position:absolute;left:9px;right:9px;top:31px;border:0;border-top:1px solid var(--line)}
.card p{position:absolute;left:15px;font-size:11px;color:var(--text-soft);white-space:nowrap}
</style>
</head>
<body>
<div class="app">
  <header class="topbar"><h1>Welcome to <b>Nexa form</b></h1></header>

  <aside class="sidebar">
    <div class="profile">
      <div class="avatar" role="img" aria-label="User profile photo"></div>
      <div class="name">Marco Delvina</div>
      <div class="role">Administrator</div>
      <svg class="caret" width="13" height="8" viewBox="0 0 13 8"><path d="M0 0h13L6.5 8z" fill="var(--brand)"/></svg>
    </div>

    <div class="group"></div>
    <ul class="nav">
      <li class="nav-item" style="top:148px">
        <svg viewBox="0 0 18 18" fill="none" stroke="#c5c7cf" stroke-width="1.3"><path d="M2 13a7 7 0 0 1 14 0"/><path d="M9 13l3-5"/></svg>
        <span class="label">Dashboard</span><span class="badge" style="background:var(--badge-blue)">3</span>
      </li>
      <li class="nav-item" style="top:196px">
        <svg viewBox="0 0 18 18" fill="none" stroke="#c5c7cf" stroke-width="1.3"><path d="M9 15S2 10.5 2 6.3A3.3 3.3 0 0 1 9 5a3.3 3.3 0 0 1 7 1.3C16 10.5 9 15 9 15z"/></svg>
        <span class="label">Services</span><span class="badge" style="background:var(--badge-pink)">2</span>
      </li>
      <li class="nav-item" style="top:243px">
        <svg viewBox="0 0 18 18" fill="none" stroke="#c5c7cf" stroke-width="1.3"><rect x="7" y="1.5" width="4" height="4"/><path d="M9 5.5v4M3 16V9.5h12V16M9 9.5V16"/></svg>
        <span class="label">connectors</span>
      </li>
      <li class="nav-item" style="top:291px">
        <svg viewBox="0 0 18 18" fill="none" stroke="#c5c7cf" stroke-width="1.3"><path d="M1.5 14l5-5 3 3 7-7"/></svg>
        <span class="label">Ingestion</span><span class="badge" style="background:var(--badge-green)">1</span>
      </li>
      <li class="nav-item active" style="top:338px">
        <svg viewBox="0 0 18 18" fill="none" stroke="#c5c7cf" stroke-width="1.3"><circle cx="9" cy="9" r="2.5"/><circle cx="9" cy="9" r="6.5" stroke-dasharray="3 1.5"/></svg>
        <span class="label">Workbench</span>
      </li>
      <li class="sub" style="top:370px">Projects</li>
      <li class="sub" style="top:402px">Schemas</li>
      <li class="sub" style="top:433px">Streams</li>
      <li class="sub" style="top:465px">Model management</li>
      <li class="sub" style="top:497px">Deployments</li>
      <li class="nav-item" style="top:560px">
        <svg viewBox="0 0 18 18" fill="none" stroke="#c5c7cf" stroke-width="1.3"><circle cx="9" cy="5.5" r="3.5"/><path d="M2 16.5c0-3.5 3-5.5 7-5.5s7 2 7 5.5z"/></svg>
        <span class="label">Administration</span><span class="badge" style="background:var(--badge-red)">5</span>
      </li>
    </ul>
  </aside>

  <div class="create-btn">Create a project</div>

  <section class="projects">
    <div class="card" style="left:293px;top:188px"><h3>WINE MODEL</h3><svg class="kebab" width="4" height="14"><circle cx="2" cy="2" r="1.4" fill="var(--brand)"/><circle cx="2" cy="7" r="1.4" fill="var(--brand)"/><circle cx="2" cy="12" r="1.4" fill="var(--brand)"/></svg><hr><p style="top:43px">Description : This project is awesome..</p><p style="top:69px">Created by: Tomas</p><p style="top:95px">Created date: April 4, 2019</p><p style="top:121px">Version: 1.2</p></div>
    <div class="card" style="left:531px;top:188px"><h3>CUSTOMERSEG</h3><svg class="kebab" width="4" height="14"><circle cx="2" cy="2" r="1.4" fill="var(--brand)"/><circle cx="2" cy="7" r="1.4" fill="var(--brand)"/><circle cx="2" cy="12" r="1.4" fill="var(--brand)"/></svg><hr><p style="top:43px">Description : This project is awesome..</p><p style="top:69px">Created by: Tomas</p><p style="top:95px">Created date: April 4, 2019</p><p style="top:121px">Version: 1.2</p></div>
    <div class="card" style="left:770px;top:188px"><h3>WINE MODEL</h3><svg class="kebab" width="4" height="14"><circle cx="2" cy="2" r="1.4" fill="var(--brand)"/><circle cx="2" cy="7" r="1.4" fill="var(--brand)"/><circle cx="2" cy="12" r="1.4" fill="var(--brand)"/></svg><hr><p style="top:43px">Description : This project is awesome..</p><p style="top:69px">Created by: Tomas</p><p style="top:95px">Created date: April 4, 2019</p><p style="top:121px">Version: 1.2</p></div>

    <div class="card" style="left:293px;top:377px"><h3>WINE MODEL</h3><svg class="kebab" width="4" height="14"><circle cx="2" cy="2" r="1.4" fill="var(--brand)"/><circle cx="2" cy="7" r="1.4" fill="var(--brand)"/><circle cx="2" cy="12" r="1.4" fill="var(--brand)"/></svg><hr><p style="top:43px">Description : This project is awesome..</p><p style="top:69px">Created by: Tomas</p><p style="top:95px">Created date: April 4, 2019</p><p style="top:121px">Version: 1.2</p></div>
    <div class="card" style="left:531px;top:377px"><h3>CUSTOMERSEG</h3><svg class="kebab" width="4" height="14"><circle cx="2" cy="2" r="1.4" fill="var(--brand)"/><circle cx="2" cy="7" r="1.4" fill="var(--brand)"/><circle cx="2" cy="12" r="1.4" fill="var(--brand)"/></svg><hr><p style="top:43px">Description : This project is awesome..</p><p style="top:69px">Created by: Tomas</p><p style="top:95px">Created date: April 4, 2019</p><p style="top:121px">Version: 1.2</p></div>
    <div class="card" style="left:770px;top:377px"><h3>WINE MODEL</h3><svg class="kebab" width="4" height="14"><circle cx="2" cy="2" r="1.4" fill="var(--brand)"/><circle cx="2" cy="7" r="1.4" fill="var(--brand)"/><circle cx="2" cy="12" r="1.4" fill="var(--brand)"/></svg><hr><p style="top:43px">Description : This project is awesome..</p><p style="top:69px">Created by: Tomas</p><p style="top:95px">Created date: April 4, 2019</p><p style="top:121px">Version: 1.2</p></div>

    <div class="card" style="left:293px;top:572px"><h3>WINE MODEL</h3><svg class="kebab" width="4" height="14"><circle cx="2" cy="2" r="1.4" fill="var(--brand)"/><circle cx="2" cy="7" r="1.4" fill="var(--brand)"/><circle cx="2" cy="12" r="1.4" fill="var(--brand)"/></svg><hr><p style="top:43px">Description : This project is awesome..</p><p style="top:69px">Created by: Tomas</p><p style="top:95px">Created date: April 4, 2019</p><p style="top:121px">Version: 1.2</p></div>
    <div class="card" style="left:531px;top:572px"><h3>CUSTOMERSEG</h3><svg class="kebab" width="4" height="14"><circle cx="2" cy="2" r="1.4" fill="var(--brand)"/><circle cx="2" cy="7" r="1.4" fill="var(--brand)"/><circle cx="2" cy="12" r="1.4" fill="var(--brand)"/></svg><hr><p style="top:43px">Description : This project is awesome..</p><p style="top:69px">Created by: Tomas</p><p style="top:95px">Created date: April 4, 2019</p><p style="top:121px">Version: 1.2</p></div>
    <div class="card" style="left:770px;top:572px"><h3>WINE MODEL</h3><svg class="kebab" width="4" height="14"><circle cx="2" cy="2" r="1.4" fill="var(--brand)"/><circle cx="2" cy="7" r="1.4" fill="var(--brand)"/><circle cx="2" cy="12" r="1.4" fill="var(--brand)"/></svg><hr><p style="top:43px">Description : This project is awesome..</p><p style="top:69px">Created by: Tomas</p><p style="top:95px">Created date: April 4, 2019</p><p style="top:121px">Version: 1.2</p></div>
  </section>
</div>
</body>
</html>
```